Oven Cleaning flyer design

Hi there,
I need help designing a letterbox flyer. It needs to be DL size.
I have attached a rough design made with Chat GPT.
Would like back and front, have my business colors.
Please find attached mock up of what I would roughly like.
Also find attached logo.
Thank you

Target Market(s)

Home owners over 40

Industry/Entity Type

Cleaning

Requirements
Must have
• Logo, before after of oven, brand colors

```html
<!DOCTYPE html>
<html lang="en">
<head>
<meta charset="utf-8">
<title>Gleam Oven Care – DL Flyer</title>
<link rel="stylesheet" href="https://fonts.googleapis.com/css2?family=Krona+One&family=Poppins:wght@400;500;600;700&family=Roboto+Condensed:wght@600;700&display=swap">
<style>
  :root {
    --stage: #555555;
    --ink: #000000;
    --teal: #47c1c8;
    --white: #ffffff;
    --gold: #c9a227;
    --photo-dark: #3b3a38;
    --photo-warm: #8a6a45;
    --photo-light: #c9cdd0;
  }
  * { margin: 0; padding: 0; box-sizing: border-box; }
  html, body { width: 1200px; height: 1150px; overflow: hidden; background: var(--stage); }
  .panel {
    position: absolute; top: 80px; width: 482px; height: 990px;
    background: var(--ink); overflow: hidden; color: var(--white);
  }
  .panel--front { left: 95px; }
  .panel--back { left: 612px; }
  .panel > svg.backdrop { position: absolute; inset: 0; }
  .abs { position: absolute; }
  .display { font-family: "Krona One", sans-serif; }
  .condensed { font-family: "Roboto Condensed", sans-serif; font-weight: 600; }
  .sans { font-family: "Poppins", sans-serif; }
  .teal { color: var(--teal); }

  /* front */
  .brand { left: 100px; top: 22px; display: flex; align-items: center; gap: 14px; }
  .brand__dot { width: 62px; height: 62px; border-radius: 50%; background: var(--teal); }
  .brand__name { font-family: "Krona One", sans-serif; font-size: 21px; line-height: 1.25; color: var(--teal); }
  .headline { left: 0; width: 482px; top: 128px; text-align: center; font-size: 34px; line-height: 41px; padding-left: 95px; }
  .tag { top: 407px; height: 35px; width: 102px; background: var(--teal); font-family: "Roboto Condensed", sans-serif; font-weight: 700; font-size: 23px; line-height: 35px; text-align: center; color: var(--white); }
  .tag--before { left: 125px; }
  .tag--after { left: 239px; }
  .pitch { left: 0; width: 482px; padding-left: 16px; top: 682px; text-align: center; font-size: 21px; line-height: 25px; }
  .rule { left: 17px; width: 449px; top: 819px; height: 1.5px; background: var(--teal); }
  .cta { left: 0; width: 482px; top: 829px; text-align: center; font-size: 19px; font-weight: 600; padding-right: 6px; }
  .phone { display: flex; align-items: center; gap: 7px; }
  .phone__icon { width: 52px; height: 52px; border-radius: 50%; background: var(--teal); display: flex; align-items: center; justify-content: center; }
  .phone__number { font-family: "Poppins", sans-serif; font-weight: 600; font-size: 49px; letter-spacing: -1px; line-height: 1; }
  .phone--front { left: 64px; top: 871px; }
  .web-band { left: 0; width: 482px; top: 934px; height: 41px; background: var(--teal); text-align: center; font-family: "Poppins", sans-serif; font-weight: 500; font-size: 26px; line-height: 41px; padding-right: 14px; }

  /* back */
  .why { left: 0; width: 482px; top: 26px; text-align: center; font-size: 33px; line-height: 1.1; padding-left: 16px; }
  .why__sub { display: block; font-size: 21px; margin-top: 14px; padding-left: 8px; }
  .reasons { left: 98px; top: 118px; width: 370px; list-style: none; font-size: 16.5px; line-height: 19.5px; }
  .reasons li { position: relative; padding-left: 26px; margin-bottom: 14.5px; }
  .reasons li::before { content: ""; position: absolute; left: 2px; top: 3px; width: 14px; height: 14px; border-radius: 50%; background: var(--teal); border: 2px solid var(--white); }
  .offer { left: 0; width: 482px; top: 498px; text-align: center; }
  .offer__lead { font-weight: 400; font-size: 28px; line-height: 1.2; padding-right: 20px; }
  .offer__deal { font-weight: 700; font-size: 36px; line-height: 1.2; margin-top: 6px; }
  .offer__deal b { color: var(--ink); }
  .perks { left: 51px; top: 608px; list-style: none; }
  .perks li { display: flex; align-items: center; gap: 12px; height: 46px; font-family: "Poppins", sans-serif; font-weight: 600; font-size: 25px; }
  .tick { width: 32px; height: 32px; border-radius: 50%; background: var(--white); display: flex; align-items: center; justify-content: center; flex: none; }
  .phone--back { left: 54px; top: 773px; }
  .web-back { left: 0; width: 482px; top: 832px; text-align: center; font-family: "Poppins", sans-serif; font-weight: 500; font-size: 28px; padding-left: 2px; }
  .extras-band { left: 0; width: 482px; top: 888px; height: 102px; background: var(--teal); text-align: center; font-family: "Poppins", sans-serif; font-weight: 600; font-size: 19px; line-height: 34px; padding-top: 17px; }
</style>
</head>
<body>

<section class="panel panel--front" aria-label="Flyer front">
  <svg class="backdrop" width="482" height="990" viewBox="0 0 482 990" aria-hidden="true">
    <defs>
      <clipPath id="photo-window">
        <path d="M0,440 C80,385 170,355 245,365 C330,378 420,430 482,510 L482,722 C420,665 350,635 291,640 C180,650 80,720 0,796 Z"/>
      </clipPath>
      <linearGradient id="before-fill" x1="0" y1="0" x2="0" y2="1">
        <stop offset="0" stop-color="var(--photo-light)"/>
        <stop offset="0.35" stop-color="var(--photo-dark)"/>
        <stop offset="1" stop-color="var(--photo-warm)"/>
      </linearGradient>
      <linearGradient id="after-fill" x1="0" y1="0" x2="0" y2="1">
        <stop offset="0" stop-color="var(--photo-light)"/>
        <stop offset="0.4" stop-color="var(--photo-dark)"/>
        <stop offset="1" stop-color="#6f7478"/>
      </linearGradient>
    </defs>
    <path d="M0,275 C110,300 250,330 340,395 L482,540 L482,990 L0,990 Z" fill="var(--teal)"/>
    <path d="M0,0 L38,0 C60,150 160,290 340,388 C170,320 45,215 0,120 Z" fill="var(--white)"/>
    <path d="M0,230 C110,280 240,320 345,392 C230,352 100,318 0,282 Z" fill="var(--white)"/>
    <path d="M0,400 C100,350 210,330 300,360 C380,390 440,440 482,500 L482,520 C420,440 330,385 245,378 C160,372 70,410 0,455 Z" fill="var(--white)"/>
    <g clip-path="url(#photo-window)">
      <rect x="0" y="340" width="226" height="470" fill="url(#before-fill)" role="img" aria-label="Photo of a dirty oven interior before cleaning"/>
      <rect x="226" y="340" width="11" height="470" fill="var(--white)"/>
      <rect x="237" y="340" width="245" height="470" fill="url(#after-fill)" role="img" aria-label="Photo of the same oven interior after cleaning"/>
    </g>
    <path d="M0,796 C80,720 180,650 291,640 C380,635 440,680 482,722 L482,990 L0,990 Z" fill="var(--ink)"/>
    <path d="M0,796 C80,720 180,650 291,640 C350,637 400,655 440,680" fill="none" stroke="var(--white)" stroke-width="4"/>
  </svg>

  <div class="abs brand">
    <span class="brand__dot"></span>
    <span class="brand__name">GLEAM<br>OVEN CARE</span>
  </div>

  <h1 class="abs headline display">BRING YOUR<br><span class="teal">OVEN BACK</span><br>TO LIFE</h1>

  <div class="abs tag tag--before">BEFORE</div>
  <div class="abs tag tag--after">AFTER</div>

  <p class="abs pitch condensed">Professional,<br><span class="teal">non-caustic oven cleaning</span><br>that removes built-up grease, smoke,<br>and bunt grime - leaving your<br>oven looking fresh again.</p>

  <div class="abs rule"></div>
  <p class="abs cta sans">Call Now for Fast, Professional Service</p>

  <div class="abs phone phone--front">
    <span class="phone__icon">
      <svg width="26" height="26" viewBox="0 0 24 24" aria-hidden="true"><path d="M6.6 10.8a15 15 0 0 0 6.6 6.6l2.2-2.2a1 1 0 0 1 1-.25 11.4 11.4 0 0 0 3.6.57 1 1 0 0 1 1 1V20a1 1 0 0 1-1 1A17 17 0 0 1 3 4a1 1 0 0 1 1-1h3.5a1 1 0 0 1 1 1c0 1.25.2 2.45.57 3.57a1 1 0 0 1-.25 1Z" fill="none" stroke="#fff" stroke-width="1.6"/></svg>
    </span>
    <span class="phone__number">0400 123 987</span>
  </div>

  <div class="abs web-band">gleamovencare.com.au</div>
</section>

<section class="panel panel--back" aria-label="Flyer back">
  <svg class="backdrop" width="482" height="990" viewBox="0 0 482 990" aria-hidden="true">
    <path d="M0,104 C40,230 150,360 343,462 C200,420 60,300 0,200 Z" fill="var(--white)"/>
    <path d="M6,120 C30,190 60,240 90,270 C60,250 30,200 6,140 Z" fill="var(--gold)"/>
    <path d="M0,214 C50,300 150,380 300,440 C180,420 60,380 0,330 Z" fill="var(--teal)"/>
    <path d="M0,325 C120,390 240,430 350,470 C220,450 90,420 0,375 Z" fill="var(--white)"/>
    <path d="M0,496 C80,450 150,430 220,432 C320,436 420,500 482,575 L482,760 L0,760 Z" fill="var(--white)"/>
    <path d="M0,536 C80,480 160,455 230,457 C330,462 420,520 482,600 L482,760 L0,760 Z" fill="var(--teal)"/>
  </svg>

  <h2 class="abs why display">WHY CHOOSE<span class="why__sub teal">GLEAM OVEN CARE?</span></h2>

  <ul class="abs reasons condensed">
    <li>We're a local family business providing professional</li>
    <li>Non-caustic oven cleaning across Sunshine Coast.</li>
    <li>Using specialized-equipment and proven cleaning methods.</li>
    <li>We remove heavy grease, carbon build-up, smoke residue, restoring your oven safely and effectively.</li>
  </ul>

  <div class="abs offer sans">
    <p class="offer__lead">Mention this flyer for</p>
    <p class="offer__deal"><b>$10 off</b> your first clean</p>
  </div>

  <ul class="abs perks">
    <li><span class="tick"><svg width="18" height="18" viewBox="0 0 24 24" aria-hidden="true"><path d="M5 12.5l4.5 4.5L19 7.5" fill="none" stroke="var(--teal)" stroke-width="3.2" stroke-linecap="round" stroke-linejoin="round"/></svg></span>Reliable Service</li>
    <li><span class="tick"><svg width="18" height="18" viewBox="0 0 24 24" aria-hidden="true"><path d="M5 12.5l4.5 4.5L19 7.5" fill="none" stroke="var(--teal)" stroke-width="3.2" stroke-linecap="round" stroke-linejoin="round"/></svg></span>Non-Caustic Cleaning</li>
    <li><span class="tick"><svg width="18" height="18" viewBox="0 0 24 24" aria-hidden="true"><path d="M5 12.5l4.5 4.5L19 7.5" fill="none" stroke="var(--teal)" stroke-width="3.2" stroke-linecap="round" stroke-linejoin="round"/></svg></span>Satisfaction Guaranteed</li>
  </ul>

  <div class="abs phone phone--back">
    <span class="phone__icon">
      <svg width="26" height="26" viewBox="0 0 24 24" aria-hidden="true"><path d="M6.6 10.8a15 15 0 0 0 6.6 6.6l2.2-2.2a1 1 0 0 1 1-.25 11.4 11.4 0 0 0 3.6.57 1 1 0 0 1 1 1V20a1 1 0 0 1-1 1A17 17 0 0 1 3 4a1 1 0 0 1 1-1h3.5a1 1 0 0 1 1 1c0 1.25.2 2.45.57 3.57a1 1 0 0 1-.25 1Z" fill="none" stroke="#fff" stroke-width="1.6"/></svg>
    </span>
    <span class="phone__number">0400 123 987</span>
  </div>

  <p class="abs web-back teal">gleamovencare.com.au</p>

  <p class="abs extras-band">We also clean cooktops, rangehoods<br>and BBQs</p>
</section>

</body>
</html>
```